I need a book cover for my book titled Sunny Porch! The subtitle is Our Garden Years and the the author is Denisha Caldwell. I want the attached photo included on the cover, plus the words "I never met a chicken wing I didn't like!" The book size is 5.06 x 7.81 in. and is 146 pages. For the color scheme, I like a chocolate brown cover with aqua blue letters. (Please note that you don't have to use these colors. Feel free to use this color scheme or whatever you colors you like!)

• Please include my photo for the back cover, along with this text:

Sunny Porch! I was tired of being tired! I was tired of acid reflux, body stiffness, and being overweight. To make matters worse, I suffered from back pain, constipation, leg pain, and lack of sleep. If you are tired of looking to medical test for your answers, this is the book for you. The key was the day I decided to make “me” a priority by being #1 on my “to-do” list.

Our healthcare system seems to be more concerned about treating illness than they are about preventing it; which is why we have so many problems with our health and wellness. That’s why I’m going to give you insights into nutrition, health care, and the pharmaceutical industry.

I’m also going to give you some insights into exercise, supplements, detoxing and essential oils; as well as what goes into your grocery cart and the foods you feed your family.

Because you’re reading this I know you’re ready to live your best life, Sunny Porch! is for you.

Here’s to a healthy you!

Here's a brief bio about the author for the back cover:

Denisha lives in Chicago with her husband, Dr. Marvin, and has three adult children. She is probably one of the most private people you will meet – BUT HAD to tell her story!

```html
<!DOCTYPE html>
<html lang="en">
<head>
<meta charset="utf-8">
<title>Sunny Porch! – Book Cover</title>
<link rel="stylesheet" href="https://fonts.googleapis.com/css2?family=Cabin:wght@600&family=Open+Sans:wght@600&family=Permanent+Marker&family=Space+Mono&display=swap">
<style>
  :root {
    --chocolate: #4a261b;
    --band: #8a2a20;
    --aqua: #00f0f0;
    --teal: #1b8584;
    --cream: #efe7e2;
    --white: #ffffff;
    --spine-line: #2a120c;
  }
  html, body { margin: 0; padding: 0; overflow: hidden; background: var(--chocolate); }
  .cover {
    position: relative;
    width: 1200px; height: 882px;
    background: var(--chocolate);
    overflow: hidden;
  }
  .band { position: absolute; left: 0; width: 1200px; background: var(--band); }
  .band--top { top: 0; height: 22px; }
  .band--bottom { bottom: 0; height: 37px; }
  .spine-edge { position: absolute; width: 1px; background: var(--spine-line); }
  .spine-edge--left { left: 572px; }
  .spine-edge--right { left: 625px; }
  .spine-edge--top { top: 0; height: 44px; }
  .spine-edge--bottom { bottom: 0; height: 42px; }

  .author-photo {
    position: absolute; left: 227px; top: 65px;
    width: 134px; height: 175px; border-radius: 50%;
    background: radial-gradient(ellipse at 50% 45%, #8a6a5c 0%, #6e5044 55%, #5a4036 100%);
  }
  .blurb {
    position: absolute; left: 32px; top: 248px; width: 513px;
    font-family: "Cabin", sans-serif; font-weight: 600;
    font-size: 16px; line-height: 21.4px; color: var(--white);
    text-align: justify;
  }
  .blurb p { margin: 0 0 21.4px; }
  .blurb .lead { color: var(--aqua); }
  .bio {
    position: absolute; left: 32px; top: 752px; width: 513px;
    font-family: "Cabin", sans-serif; font-weight: 600;
    font-size: 14px; line-height: 18.7px; color: var(--white);
    text-align: justify; margin: 0;
  }

  .spine-text { position: absolute; left: 572px; top: 0; }
  .front-type { position: absolute; left: 0; top: 0; }
  .title { font-family: "Open Sans", sans-serif; font-weight: 600; fill: var(--aqua); }
  .subtitle { font-family: "Permanent Marker", cursive; fill: var(--white); }
  .tagline { font-family: "Space Mono", monospace; fill: var(--cream); }
  .author-name { font-family: "Space Mono", monospace; fill: var(--teal); }

  .hero-photo {
    position: absolute; left: 646px; top: 232px;
    width: 528px; height: 456px;
    border-radius: 30px;
    background: radial-gradient(ellipse at 62% 62%, #c4421c 0%, #a5472c 30%, #d9d4cf 55%, rgba(74,38,27,0) 75%);
  }
</style>
</head>
<body>
<div class="cover">
  <div class="band band--top"></div>
  <div class="band band--bottom"></div>
  <div class="spine-edge spine-edge--left spine-edge--top"></div>
  <div class="spine-edge spine-edge--right spine-edge--top"></div>
  <div class="spine-edge spine-edge--left spine-edge--bottom"></div>
  <div class="spine-edge spine-edge--right spine-edge--bottom"></div>

  <!-- Back cover -->
  <div class="author-photo" role="img" aria-label="Portrait photo of the author, Denisha Caldwell"></div>
  <div class="blurb">
    <p><span class="lead">Sunny Porch!</span> I was tired of being tired! I was tired of acid reflux, body stiffness, and being overweight. To make matters worse, I suffered from back pain, constipation, leg pain, and lack of sleep. If you are tired of looking to medical test for your answers, this is the book for you. The key was the day I decided to make “me” a priority by being #1 on my “to-do” list.</p>
    <p>Our healthcare system seems to be more concerned about treating illness than they are about preventing it; which is why we have so many problems with our health and wellness. That’s why I’m going to give you insights into nutrition, health care, and the pharmaceutical industry.</p>
    <p>I’m also going to give you some insights into exercise, supplements, detoxing and essential oils; as well as what goes into your grocery cart and the foods you feed your family.</p>
    <p>Because you’re reading this I know you’re ready to live your best life, Sunny Porch! is for you.</p>
    <p>Here’s to a healthy you!</p>
  </div>
  <p class="bio">Denisha lives in Chicago with her husband, Dr. Marvin, and has three adult children. She is probably one of the most private people you will meet – BUT HAD to tell her story!</p>

  <!-- Spine -->
  <svg class="spine-text" width="53" height="882" viewBox="0 0 53 882">
    <text class="title" transform="translate(17 76) rotate(90)" font-size="30" textLength="400" lengthAdjust="spacing">SUNNY PORCH!</text>
    <text class="subtitle" transform="translate(18 574) rotate(90)" font-size="22" textLength="232" lengthAdjust="spacingAndGlyphs">OUR GARDEN YEARS</text>
  </svg>

  <!-- Front cover -->
  <div class="hero-photo" role="img" aria-label="Photo of glazed chicken wings with celery, carrot sticks and a dip cup in a white dish printed with warning signs"></div>
  <svg class="front-type" width="1200" height="882" viewBox="0 0 1200 882">
    <text class="title" x="651" y="135" font-size="88" textLength="518" lengthAdjust="spacingAndGlyphs">SUNNY PORCH!</text>
    <text class="subtitle" x="654" y="200" font-size="46" textLength="512" lengthAdjust="spacingAndGlyphs">OUR GARDEN YEARS</text>
    <text class="tagline" x="655" y="726" font-size="15" textLength="514" lengthAdjust="spacing">"I NEVER MET A CHICKEN WING I DIDN'T LIKE!"</text>
    <text class="author-name" x="651" y="810" font-size="34" textLength="518" lengthAdjust="spacing">Denisha Caldwell</text>
  </svg>
</div>
</body>
</html>
```